Website Design for a chemical distribution company

Designer must provide full implementation/coding depending on the platform chosen by the client we'd prefer wordpress type CMS system.

We need a modern and bold website setup for our chemical distribution company. It will need to be like a web store however, no purchases take place on the website only inquiries. So for example the customer can go to a product and click on a button that brings up an inquiry window, they populate that with their information and it sends me an email with the inquiry.

We need it done 3 times pretty much the same but maybe a different colour scheme for each industry. for example on the welcome screen we want 3 icons /pictures ie: plastic, resin, industrial. When the customer clicks on the industry they need it directs them to the specific area that is perhaps on a subdomain or somewhere on the main domain but with no relation to the other industries I hope this makes sense. The layout would be the same but their should be some difference such as colours etc.

The site needs to have a powerful search engine that is very accurate.

It will have about 40,000 products and needs to be able to upload our products via an excel spreed sheet.

We need it to look graphically amazing and very easy to use for the customer.

It will also need to have a blog section that we can upload blogs to daily with different sub categories for things such as experiments, news etc.

The front page needs to be have a banner/advertisement window that is easy for us to change with new specials/deals that we bring out.

Basically the site needs to be easy to navigate, easy to get to products and inquire and needs to have a wow factor.

We also need a special requess page that gives the customers the facility to request a product that they can't find on our website.

I need to stress the importance of a search engine on the site that can handle searching through all the products.

We will also give you the words and you will need to put those on to the pages.

You will also be required to upload our catalogue via CSV or Excel to the site on final completion.

Please find similar websites below for companies that similar to us:

www.tarbexo.com
www.kovrel-dunmark.com
http://www.lumbridlab.com.au
Updates

Just to clarify only one of the websites will have 40-50k products the other 2 industries will only have about 200-500 products each. Added Sunday, February 14, 2016

Target Market(s)

Chemicals, Food, Pharmaceuticals, Business to Business

Industry/Entity Type

It Company

Coding

Coded - Design and coding required

Number of Pages Required

5+ page

Font styles to use
Sans Serif

Requirements
Must have
• Powerful search engine
• Great design
• Easy to use CMS
• SEO
• Mobile Device Compatible

```html
<!DOCTYPE html>
<html lang="en">
<head>
<meta charset="utf-8">
<title>Velkor – Chemical Distribution</title>
<link href="https://fonts.googleapis.com/css2?family=Arimo:wght@400;700&display=swap" rel="stylesheet">
<style>
:root{
  --blue:#0a78c2;
  --blue-mid:#1e8ac4;
  --head:#1c7fc3;
  --page:#dfe2e4;
  --top:#dcdfe1;
  --ink:#333;
  --dark:#262626;
  --foot-text:#d6d6d6;
  --white:#fff;
}
*{margin:0;padding:0;box-sizing:border-box}
html,body{width:722px;height:1200px;overflow:hidden}
body{font-family:"Arimo",Arial,sans-serif;color:var(--ink);background:var(--page);position:relative}
.abs{position:absolute}
.topbar{left:0;top:0;width:722px;height:53px;background:var(--top);border-top:2px solid var(--blue)}
.brand{left:190px;top:18px;font-size:17px;font-weight:400;letter-spacing:3px;color:var(--ink)}
.brand-mark{display:inline-block;width:8px;height:8px;background:var(--ink);margin-right:6px;vertical-align:middle}
.btn-sm{top:24px;height:9px;border:1px solid #aab;background:#f4f4f4;font-size:5px;line-height:7px;padding:0 6px;color:#223}
.search{left:463px;top:24px;width:58px;height:9px;border:1px solid #aab;background:#fff;font-size:5px;padding-left:4px;line-height:7px}
.search-btn{left:524px;top:24px;width:11px;height:9px;background:#2a9be0}
.cart{left:478px;top:9px;font-size:5px}
.nav{left:0;top:53px;width:722px;height:20px;background:var(--blue);display:flex;justify-content:center;align-items:center;gap:6px;color:#fff;font-size:6px;font-weight:700}
.nav .sep{opacity:.8}
.hero{left:0;top:73px;width:722px;height:219px;background:linear-gradient(90deg,#7b8fb0 0%,#c7ccd4 30%,#d9dcdf 70%,#c4b9a8 100%)}
.panel{top:84px;width:94px;height:198px;color:#fff;text-align:center}
.panel h3{margin-top:87px;font-size:13px;font-weight:700}
.panel p{font-size:5px;font-weight:700}
.arrow{top:170px;color:#fff;font-size:24px}
.band{left:0;top:292px;width:722px;height:20px;background:var(--blue)}
.h2{font-size:14px;font-weight:700;color:var(--head)}
.small{font-size:5px;line-height:6.4px}
.about-text{left:180px;top:339px;width:182px}
.about-img{left:368px;top:323px;width:167px;height:93px;background:linear-gradient(135deg,#6a6f74 0%,#a8a060 55%,#3a3e44 100%)}
.svc-title{font-size:6px;font-weight:700}
.svc-text{width:68px;color:#555}
.more{font-size:5px;color:var(--blue);font-weight:700}
.featured{left:0;top:585px;width:722px;height:133px;background:var(--blue-mid)}
.prod{top:634px;width:79px;height:61px;background:linear-gradient(180deg,#e7e7e7,#cfcfcf)}
.prod-label{top:702px;width:79px;text-align:center;color:#fff;font-size:5px;font-weight:700}
.read-btn{background:var(--blue);color:#fff;font-size:5px;font-weight:700;padding:1px 3px}
.field{width:115px;height:10px;background:#fff;border:1px solid #aaa;font-size:5px;padding-left:4px;line-height:8px}
.blog{left:0;top:990px;width:722px;height:90px;background:var(--blue)}
.rss{width:10px;height:10px;border-radius:2px;background:#f08a24}
.footer{left:0;top:1080px;width:722px;height:100px;background:var(--dark)}
.f-head{font-size:5.5px;font-weight:700;color:#fff}
.f-list{font-size:5px;line-height:11px;color:var(--foot-text)}
.bottom{left:0;top:1180px;width:722px;height:20px;background:var(--blue)}
.circ{width:8px;height:8px;border-radius:50%}
</style>
</head>
<body>
<header>
  <div class="abs topbar"></div>
  <div class="abs brand"><span class="brand-mark"></span>VELKOR</div>
  <div class="abs btn-sm" style="left:364px">Register</div>
  <div class="abs btn-sm" style="left:403px">Login</div>
  <div class="abs cart">Cart item ( 0 )</div>
  <div class="abs search">Search</div>
  <div class="abs search-btn"></div>
  <nav class="abs nav">
    <span>Home</span><span class="sep">|</span><span>About</span><span class="sep">|</span><span>Products</span><span class="sep">|</span><span>Applications</span><span class="sep">|</span><span>Services</span><span class="sep">|</span><span>Aftermarket</span><span class="sep">|</span><span>Gallery</span><span class="sep">|</span><span>Contact</span>
  </nav>
</header>

<section class="abs hero" role="img" aria-label="Laboratory glassware background photo"></section>
<div class="abs panel" style="left:212px;background:linear-gradient(160deg,#e0407a,#36b0e0 45%,#ecc23a 75%,#5bc25a)" role="img" aria-label="Coloured plastic beads photo"><h3>PLASTIC</h3><p>CHEMISTRY SECTORS</p></div>
<div class="abs panel" style="left:315px;background:linear-gradient(180deg,#2e2a22,#4a3e2c)" role="img" aria-label="Resin granules photo"><h3>RESIN</h3><p>INNOVETVE BENIFITS</p></div>
<div class="abs panel" style="left:416px;background:linear-gradient(180deg,#1d2126,#3a3f45)" role="img" aria-label="Industrial plant photo"><h3>INDUSTRIAL</h3><p>PRODUCT STEWARDSHIP</p></div>
<div class="abs arrow" style="left:184px">&#10094;</div>
<div class="abs arrow" style="left:526px">&#10095;</div>
<div class="abs band"></div>

<section>
  <div class="abs h2" style="left:180px;top:321px">ABOUT VELKOR</div>
  <div class="abs small about-text">Velkor is recognised for its innovative approach to the design and manufacture of equipment to meet specific needs within the international mining industry.<br>With the primary focus on leaching, adsorption and elution circuits, Velkor has the in-house expertise to assist with scoping, sizing, supply, installation and commissioning of capital equipment. Added to this, Velkor offers an aftermarket service to support all equipment. A team of skilled and experienced specialists interface with customers to provide optimum solutions to client requirements.</div>
  <div class="abs" style="left:180px;top:403px;font-size:5px;font-weight:700">Find out more <span style="color:var(--blue)">&gt;&gt;&gt;</span></div>
  <div class="abs about-img" role="img" aria-label="Engineer standing beside plant equipment photo"></div>

  <div class="abs h2" style="left:180px;top:424px">OUR SERVICE</div>
  <svg class="abs" style="left:233px;top:447px" width="28" height="24" viewBox="0 0 28 24" fill="none" stroke="#1c7fc3" stroke-width="1.2"><circle cx="14" cy="5" r="3.5"/><circle cx="4" cy="19" r="3.5"/><circle cx="24" cy="19" r="3.5"/><circle cx="14" cy="14" r="3"/><path d="M14 8.5v2.5M7 17.5l4.5-2M21 17.5l-4.5-2"/></svg>
  <svg class="abs" style="left:385px;top:445px" width="18" height="26" viewBox="0 0 18 26" fill="#1c7fc3"><rect x="1" y="1" width="1.2" height="8"/><rect x="3.4" y="1" width="1.2" height="8"/><rect x="5.8" y="1" width="1.2" height="8"/><rect x="3" y="8" width="2" height="17"/><path d="M13 1c3 0 4 5 3 10h-1v14h-2z"/></svg>
  <svg class="abs" style="left:241px;top:521px" width="18" height="18" viewBox="0 0 18 18" fill="none" stroke="#1c7fc3" stroke-width="1.2"><path d="M7 1h4v6h6v4h-6v6H7v-6H1V7h6z"/></svg>
  <svg class="abs" style="left:377px;top:519px" width="26" height="20" viewBox="0 0 26 20"><circle cx="5" cy="7" r="3" fill="#1c7fc3"/><rect x="1" y="11" width="8" height="9" fill="#1c7fc3"/><rect x="10" y="1" width="15" height="11" fill="none" stroke="#1c7fc3" stroke-width="1.2"/><path d="M13 10V7M16 10V4M19 10V6M22 10V3" stroke="#1c7fc3" stroke-width="1.5"/></svg>

  <div class="abs svc-title" style="left:267px;top:457px">Chemicals</div>
  <div class="abs small svc-text" style="left:267px;top:470px">Praesent vestibulum mestie lacus. Aenean nonummy hendrerit mauris. Phasellus porta..</div>
  <div class="abs more" style="left:267px;top:502px">Read more...</div>
  <div class="abs svc-title" style="left:409px;top:457px">Food</div>
  <div class="abs small svc-text" style="left:409px;top:470px">Praesent vestibulum mestie lacus. Aenean nonummy hendrerit mauris. Phasellus porta..</div>
  <div class="abs more" style="left:409px;top:502px">Read more...</div>
  <div class="abs svc-title" style="left:267px;top:526px">Pharmaceuticals</div>
  <div class="abs small svc-text" style="left:267px;top:538px">Praesent vestibulum mestie lacus. Aenean nonummy hendrerit mauris. Phasellus porta..</div>
  <div class="abs more" style="left:267px;top:570px">Read more...</div>
  <div class="abs svc-title" style="left:409px;top:526px">Business</div>
  <div class="abs small svc-text" style="left:409px;top:538px">Praesent vestibulum mestie lacus. Aenean nonummy hendrerit mauris. Phasellus porta..</div>
  <div class="abs more" style="left:409px;top:570px">Read more...</div>
</section>

<section>
  <div class="abs featured"></div>
  <div class="abs h2" style="left:180px;top:594px;color:#fff">FEATURED PRODUCTS</div>
  <div class="abs circ" style="left:182px;top:660px;border:1px solid #cde"></div>
  <div class="abs circ" style="left:532px;top:660px;border:1px solid #cde"></div>
  <div class="abs prod" style="left:191px" role="img" aria-label="Agitation tank plant render"></div>
  <div class="abs prod" style="left:277px" role="img" aria-label="Kiln equipment render"></div>
  <div class="abs prod" style="left:363px" role="img" aria-label="Electro cell render"></div>
  <div class="abs prod" style="left:452px" role="img" aria-label="MPS unit render"></div>
  <div class="abs prod-label" style="left:191px">AGITANK</div>
  <div class="abs prod-label" style="left:277px">KILN</div>
  <div class="abs prod-label" style="left:363px">ELECTRO</div>
  <div class="abs prod-label" style="left:452px">MPS</div>
</section>

<section>
  <div class="abs h2" style="left:180px;top:726px">NEWS &amp; INFORMATION</div>
  <div class="abs" style="left:191px;top:748px;font-size:5.5px;font-weight:700">L.MORVANE</div>
  <div class="abs" style="left:191px;top:759px;font-size:5px;font-weight:700">st.Louis, Mo -Feb 15,2016</div>
  <div class="abs small" style="left:191px;top:768px;width:120px">Veiat nulla facilisis at vero eros et accumsan et iusto odio dignissim qui blandit praesent luptaum zzelenit augue duis dolore te feugait nulla facilisi.</div>
  <div class="abs read-btn" style="left:249px;top:794px">READ MORE</div>
  <div class="abs" style="left:191px;top:810px;font-size:5.5px;font-weight:700">L.MORVANE</div>
  <div class="abs" style="left:191px;top:821px;font-size:5px;font-weight:700">st.Louis, Mo -Feb 15,2016</div>
  <div class="abs small" style="left:191px;top:830px;width:120px">Veiat nulla facilisis at vero eros et accumsan et iusto odio dignissim qui blandit praesent luptaum zzelenit augue duis dolore te feugait nulla facilisi.</div>
  <div class="abs read-btn" style="left:249px;top:856px">READ MORE</div>

  <div class="abs h2" style="left:360px;top:726px">NEWS LETTER SINGUP</div>
  <div class="abs small" style="left:372px;top:750px;width:130px">Latest information only. Day by day Subscribe to our newsletter to receive news updates,and special offers by email.</div>
  <div class="abs" style="left:362px;top:779px;width:140px;height:50px;border:1px solid #999"></div>
  <div class="abs field" style="left:372px;top:790px">Your name</div>
  <div class="abs field" style="left:372px;top:806px">Y our Email address</div>
  <div class="abs read-btn" style="left:362px;top:841px;padding:2px 4px;font-weight:400">Subscribe</div>

  <div class="abs h2" style="left:327px;top:872px;font-size:11px">TESTIMONIAL</div>
  <div class="abs" style="left:343px;top:894px;width:38px;height:38px;border-radius:50%;border:1px solid #666;background:linear-gradient(180deg,#8a7a6c,#c9b7a4)" role="img" aria-label="Customer portrait"></div>
  <div class="abs small" style="left:216px;top:939px;width:290px;text-align:center">After graduating from the university, I faced with the problem. There were no company where I had not heard a refusal. My friend advised me company. I have chosen a probation program. I was lucky enough to undergo a training in 'Norvale' company. That was 3 years ago, and nowadays I am a happy top-manager of this company.</div>
  <div class="abs" style="left:216px;top:966px;width:290px;text-align:center;font-size:5px;font-weight:700">Tomas Vedrani, Italy<br>Designer</div>
</section>

<section>
  <div class="abs blog"></div>
  <div class="abs h2" style="left:180px;top:998px;color:#fff">BLOG FEEDS</div>
  <div class="abs rss" style="left:191px;top:1023px"></div>
  <div class="abs" style="left:214px;top:1021px;font-size:5.5px;font-weight:700;color:#111">Praesent vestibulum molestie lacus</div>
  <div class="abs" style="left:225px;top:1028px;font-size:4.5px;color:#123">by ALAN PERRET on JAN 17, 2016</div>
  <div class="abs small" style="left:191px;top:1039px;width:145px;color:#fff">Parturient montes, nascetur ridiculus mus. Nulla dui. Fusce feugiat malesuada odio. Morbi nunc odio, gravida at, c nec, luctus a, lorem. Maecenas tristique orci ac sem</div>
  <div class="abs" style="left:296px;top:1060px;font-size:5px;font-weight:700;color:#fff">MORE INFO &lt;&lt;&lt;</div>
  <div class="abs rss" style="left:372px;top:1023px"></div>
  <div class="abs" style="left:394px;top:1021px;font-size:5.5px;font-weight:700;color:#111">Praesent vestibulum molestie lacus</div>
  <div class="abs" style="left:405px;top:1028px;font-size:4.5px;color:#123">by ALAN PERRET on JAN 17, 2016</div>
  <div class="abs small" style="left:372px;top:1039px;width:145px;color:#fff">Parturient montes, nascetur ridiculus mus. Nulla dui. Fusce feugiat malesuada odio. Morbi nunc odio, gravida at, c nec, luctus a, lorem. Maecenas tristique orci ac sem</div>
  <div class="abs" style="left:476px;top:1060px;font-size:5px;font-weight:700;color:#fff">MORE INFO &lt;&lt;&lt;</div>
</section>

<footer>
  <div class="abs footer"></div>
  <div class="abs f-head" style="left:206px;top:1090px">LINKS</div>
  <div class="abs f-list" style="left:206px;top:1102px">About us<br>Products<br>My blog<br>Custmor support</div>
  <div class="abs f-head" style="left:282px;top:1090px">CONTACT US</div>
  <div class="abs small" style="left:282px;top:1106px;width:62px;color:var(--foot-text)">12 Orrin Crescent, Halden Business Park, Westfield.<br><b>Phone:</b><br>+27 10 555 0184<br><b>Email:</b><br>marketing@velkor.com</div>
  <div class="abs f-head" style="left:373px;top:1089px">MAP</div>
  <div class="abs" style="left:373px;top:1106px;width:66px;height:50px;background:linear-gradient(135deg,#e8e4dc,#d4dccb)" role="img" aria-label="Location map"></div>
  <div class="abs f-head" style="left:474px;top:1090px">FOLLOW US ON</div>
  <div class="abs circ" style="left:475px;top:1107px;background:#3b5a9a"></div>
  <div class="abs circ" style="left:475px;top:1119px;background:#d2362b"></div>
  <div class="abs circ" style="left:475px;top:1131px;background:#1a84bc"></div>
  <div class="abs circ" style="left:475px;top:1144px;background:#2eb5e8"></div>
  <div class="abs f-list" style="left:486px;top:1105px;line-height:12.3px">friendwall<br>postly +<br>worknet<br>chirper</div>
  <div class="abs bottom"></div>
  <div class="abs" style="left:181px;top:1188px;font-size:4px;color:#fff">© Copyright 2016 Velkor (Pty) Ltd. All Rights Reserved</div>
  <div class="abs" style="left:495px;top:1188px;font-size:4px;color:#fff">Terms &amp; conditions | Sitemap</div>
</footer>
</body>
</html>
```